International Travel Technology R&D business needs a wordpress website

We are a start up team of initially 2 individuals but plan to grow our team quickly, we have deep experience in travel technology. Our goal is to provide next generation technology research and development on behalf of our clients who are leading players in the travel technology industry. Attached our logos.

Target Market(s)

Travel Technology companies

Industry/Entity Type

Travel Industry

Coding

Coded - Design and coding required

Font styles to use
Sans Serif

Requirements
Must have
• Make use of our logo and colour scheme in the attached. Has to have a sense of adventure/ stepping into the unknown but equally must convey a sense of professionalism , we are a safe pair of hands. Sample themes are in the attachment .
Nice to have
• We have identified a theme on layoutbazaar which we feel would be inspirational. We hahe attached them to help in the design as inspiration.
Should not have
• images of airplanes , hotels etc, we want to project a future image.

```html
<!DOCTYPE html>
<html lang="en">
<head>
<meta charset="utf-8">
<title>Our Services</title>
<link href="https://fonts.googleapis.com/css2?family=Michroma&family=Open+Sans:wght@400;600&family=PT+Serif&display=swap" rel="stylesheet">
<style>
  :root {
    --page: #ffffff;
    --ink: #111111;
    --ink-soft: #2b3640;
    --body-grey: #6d6d6d;
    --panel-fill: rgba(255, 255, 255, 0.22);
    --panel-line: rgba(255, 255, 255, 0.85);
    --accent: #27a6e0;
    --footer-band: #efefef;
    --sky-light: #cfe6ef;
    --sky-mid: #9fc2d6;
    --sky-deep: #6f93ad;
  }
  * { box-sizing: border-box; margin: 0; padding: 0; }
  html, body { width: 1200px; height: 1200px; overflow: hidden; background: var(--page); }
  body { position: relative; font-family: "Open Sans", sans-serif; }

  .services-hero {
    position: absolute; left: 0; top: 14px; width: 1200px; height: 524px;
    background:
      radial-gradient(ellipse at 85% 40%, rgba(80,110,140,0.55), transparent 55%),
      radial-gradient(ellipse at 10% 80%, rgba(120,150,170,0.5), transparent 60%),
      radial-gradient(ellipse at 50% 95%, rgba(150,160,150,0.45), transparent 50%),
      linear-gradient(180deg, var(--sky-light) 0%, var(--sky-mid) 55%, var(--sky-deep) 100%);
  }
  .services-panel {
    position: absolute; left: 139px; top: 56px; width: 878px; height: 413px;
    background: var(--panel-fill);
  }
  .services-frame {
    position: absolute; left: 18px; top: 15px; width: 842px; height: 383px;
    border: 1px solid var(--panel-line);
  }
  .services-intro { position: absolute; left: 31px; top: 76px; width: 240px; }
  .services-intro h1 {
    font-family: "Michroma", sans-serif; font-weight: 400; color: #fff;
    font-size: 29px; line-height: 38px; letter-spacing: 1px; padding-left: 3px;
  }
  .services-intro p {
    margin-top: 22px; color: var(--ink-soft); font-size: 12px; line-height: 20px; white-space: nowrap;
  }
  .services-divider {
    position: absolute; left: 289px; top: 70px; width: 1px; height: 274px;
    background: var(--panel-line);
  }
  .service-item { position: absolute; width: 215px; }
  .service-item svg { position: absolute; left: -46px; top: -6px; width: 32px; height: 32px; }
  .service-item h2 {
    font-family: "PT Serif", serif; font-weight: 400; font-size: 15.5px;
    color: var(--ink); letter-spacing: 0.3px; line-height: 20px; white-space: nowrap;
  }
  .service-item p {
    margin-top: 12px; font-size: 11.6px; line-height: 16.8px; color: var(--ink-soft); white-space: nowrap;
  }

  .section-title {
    position: absolute; left: 0; top: 596px; width: 1200px; text-align: center;
    font-family: "Michroma", sans-serif; font-weight: 400; font-size: 26px;
    letter-spacing: 2px; color: var(--ink);
  }
  .feature-card { position: absolute; top: 684px; width: 295px; text-align: center; }
  .feature-image { position: relative; width: 295px; height: 208px; }
  .feature-image::after {
    content: ""; position: absolute; left: 0; bottom: 0; width: 100%; height: 40px;
    background: rgba(255,255,255,0.28);
  }
  .feature-image.street { background: linear-gradient(160deg, #8a8a8a, #5a5a5a 45%, #b9b9b9); }
  .feature-image.skyline { background: linear-gradient(180deg, #eef2f1, #d6e2e3 50%, #9fb0ad); }
  .feature-image.facade { background: linear-gradient(120deg, #6b7f88, #1e3a50 50%, #0f2b43); }
  .feature-card h3 {
    margin-top: 28px; font-family: "PT Serif", serif; font-weight: 400;
    font-size: 15.5px; letter-spacing: 0.4px; color: var(--ink);
  }
  .feature-card p {
    margin: 10px auto 0; width: 275px; font-size: 11.8px; line-height: 17.6px; color: var(--body-grey);
  }
  .view-more {
    display: inline-block; margin-top: 16px; width: 114px; height: 34px; line-height: 34px;
    background: var(--accent); color: #fff; font-weight: 600; font-size: 12px;
    letter-spacing: 1px; text-decoration: none;
  }
  .footer-band {
    position: absolute; left: 0; top: 1139px; width: 1200px; height: 61px; background: var(--footer-band);
  }
</style>
</head>
<body>
  <section class="services-hero" role="img" aria-label="Blurred aerial photograph of a city skyline in pale blue haze">
    <div class="services-panel">
      <div class="services-frame"></div>
      <div class="services-intro">
        <h1>OUR<br>SERVICES</h1>
        <p>Sed do eiusmod tempor incididunt ut<br>labore et dolore magna aliqua. Ut enim<br>ad minim veniam, quis nostrud exercita-<br>tion ullamco laboris nisi ut aliquip ex ea</p>
      </div>
      <div class="services-divider"></div>

      <div class="service-item" style="left:361px; top:66px;">
        <svg viewBox="0 0 32 32" fill="none" stroke="#222" stroke-width="1.6">
          <circle cx="16" cy="16" r="4" fill="#222"/>
          <circle cx="5" cy="8" r="2.5" fill="#222"/><circle cx="27" cy="8" r="2.5" fill="#222"/>
          <circle cx="5" cy="24" r="2.5" fill="#222"/><circle cx="27" cy="24" r="2.5" fill="#222"/>
          <circle cx="16" cy="3" r="2.5" fill="#222"/><circle cx="16" cy="29" r="2.5" fill="#222"/>
          <path d="M16 16L5 8M16 16L27 8M16 16L5 24M16 16L27 24M16 16V3M16 16V29"/>
        </svg>
        <h2>EIUSMOD TEMPOR</h2>
        <p>Sed do eiusmod tempor incididunt ut<br>labore et dolore magna aliqua. Ut enim<br>ad minim veniam, quis nostrud exercita-<br>tion ullamco laboris nisi ut aliquip ex ea<br>commodo consequat. Duis aute irure</p>
      </div>
      <div class="service-item" style="left:627px; top:66px;">
        <svg viewBox="0 0 32 32" fill="none" stroke="#222" stroke-width="1.4">
          <rect x="11" y="4" width="19" height="14"/>
          <circle cx="7" cy="13" r="3"/><path d="M2 28v-6a5 5 0 0 1 10 0v6"/>
          <circle cx="21" cy="9" r="2"/><path d="M17 16a4 4 0 0 1 8 0"/>
        </svg>
        <h2>EIUSMOD TEMPOR</h2>
        <p>Sed do eiusmod tempor incididunt ut<br>labore et dolore magna aliqua. Ut enim<br>ad minim veniam, quis nostrud exercita-<br>tion ullamco laboris nisi ut aliquip ex ea<br>commodo consequat. Duis aute irure</p>
      </div>
      <div class="service-item" style="left:361px; top:230px;">
        <svg viewBox="0 0 32 32" fill="none" stroke="#222" stroke-width="1.4">
          <circle cx="12" cy="8" r="5"/><path d="M4 29v-8a8 8 0 0 1 12-6"/>
          <rect x="15" y="20" width="10" height="7"/><path d="M13 29h15"/>
        </svg>
        <h2>EIUSMOD TEMPOR</h2>
        <p>Sed do eiusmod tempor incididunt ut<br>labore et dolore magna aliqua. Ut enim<br>ad minim veniam, quis nostrud exercita-<br>tion ullamco laboris nisi ut aliquip ex ea<br>commodo consequat. Duis aute irure</p>
      </div>
      <div class="service-item" style="left:627px; top:230px;">
        <svg viewBox="0 0 32 32" fill="none" stroke="#222" stroke-width="1.8">
          <circle cx="24" cy="5" r="2.5" fill="#222"/>
          <path d="M14 12l6-3 4 5 5 1M20 9l-3 9 6 5-2 7M17 18l-5 6H7"/>
          <path d="M1 12h8M3 17h7M1 22h5"/>
        </svg>
        <h2>EIUSMOD TEMPOR</h2>
        <p>Sed do eiusmod tempor incididunt ut<br>labore et dolore magna aliqua. Ut enim<br>ad minim veniam, quis nostrud exercita-<br>tion ullamco laboris nisi ut aliquip ex ea<br>commodo consequat. Duis aute irure</p>
      </div>
    </div>
  </section>

  <h2 class="section-title">QUIS NOSTRUD</h2>

  <article class="feature-card" style="left:113px;">
    <div class="feature-image street" role="img" aria-label="Photograph of a pedestrian with an umbrella crossing a rainy city street"></div>
    <h3>NOSTRUD EXERCITATION</h3>
    <p>Sed do eiusmod tempor incididunt ut labore et dolore magna aliqua. Ut enim ad minim veniam, quis nostrud exercitation ullamco laboris nisi ut aliquip ex ea commodo consequat.</p>
    <a class="view-more" href="#">VIEW MORE</a>
  </article>
  <article class="feature-card" style="left:434px;">
    <div class="feature-image skyline" role="img" aria-label="Double-exposure photograph blending a tower skyline with a traveller"></div>
    <h3>NOSTRUD EXERCITATION</h3>
    <p>Sed do eiusmod tempor incididunt ut labore et dolore magna aliqua. Ut enim ad minim veniam, quis nostrud exercitation ullamco laboris nisi ut aliquip ex ea commodo consequat.</p>
    <a class="view-more" href="#">VIEW MORE</a>
  </article>
  <article class="feature-card" style="left:753px;">
    <div class="feature-image facade" role="img" aria-label="Upward photograph of a dark stone building facade"></div>
    <h3>NOSTRUD EXERCITATION</h3>
    <p>Sed do eiusmod tempor incididunt ut labore et dolore magna aliqua. Ut enim ad minim veniam, quis nostrud exercitation ullamco laboris nisi ut aliquip ex ea commodo consequat.</p>
    <a class="view-more" href="#">VIEW MORE</a>
  </article>

  <div class="footer-band"></div>
</body>
</html>
```